Business Card Design Project

Require a business card for a swing band called "Velvet Brass Parade". We are a 6 piece band that performs at events and corporate functions. Our music is great for dancing to or just providing a classy background atmosphere for people to enjoy. Final design should communicate professionalism and style with a hint of fun.

Sorry, just realised that it needs to be single sided only. Also, no rounded edges.

Industry/Entity Type

Events

Requirements
Must have
• Contact number: 0438 216 903
email address: velvetbrassparade@mailbox-demo.net
Website details: www.velvetbrassparade-demo.com

```html
<!DOCTYPE html>
<html lang="en">
<head>
<meta charset="utf-8">
<title>Velvet Brass Parade — Business Card</title>
<link rel="stylesheet" href="https://fonts.googleapis.com/css2?family=Bodoni+Moda:opsz,wght@6..96,400&family=Josefin+Sans:wght@300;400&display=swap">
<style>
  :root {
    --card-bg: #000000;
    --ink: #ffffff;
    --ink-soft: #f2f2f2;
  }
  html, body {
    margin: 0;
    padding: 0;
    width: 1200px;
    height: 732px;
    overflow: hidden;
    background: var(--card-bg);
  }
  .business-card {
    position: relative;
    width: 1200px;
    height: 732px;
    background: var(--card-bg);
    color: var(--ink);
    text-align: center;
  }
  .band-name {
    position: absolute;
    left: 0;
    right: 0;
    top: 200px;
    margin: 0;
    font-family: "Bodoni Moda", "Didot", serif;
    font-weight: 400;
    font-size: 86px;
    line-height: 1;
    letter-spacing: -1px;
    color: var(--ink);
  }
  .contact-list {
    position: absolute;
    left: 0;
    right: 0;
    top: 414px;
    margin: 0;
    padding: 0;
    list-style: none;
    font-family: "Josefin Sans", "Helvetica Neue", sans-serif;
    font-weight: 400;
    color: var(--ink-soft);
  }
  .contact-phone {
    font-size: 46px;
    letter-spacing: 7px;
    line-height: 58px;
    font-weight: 300;
  }
  .contact-email,
  .contact-web {
    font-size: 38px;
    font-variant: small-caps;
    letter-spacing: 3px;
    line-height: 58px;
  }
</style>
</head>
<body>
  <main class="business-card">
    <h1 class="band-name">Velvet Brass Parade</h1>
    <ul class="contact-list">
      <li class="contact-phone">0438 216 903</li>
      <li class="contact-email">velvetbrassparade@mailbox-demo.net</li>
      <li class="contact-web">www.velvetbrassparade-demo.com</li>
    </ul>
  </main>
</body>
</html>
```